Facebook Ads for HOA Law Firm

We need to create certain ads for a Facebook ads campaign. We are a law firm in Florida that represents homeowners against HOAs. We need to create the following ads:

1. Image Ads Specifications:

File Type: JPG or PNG
Ratio: 1.91:1 to 4:5
Resolution:
a) 1:1 ratio: 1080 x 1080 pixels
b) 4:5 ratio: 1080 x 1350 pixels
Maximum File Size: 30MB
Minimum Width: 600 pixels
Minimum Height:
a) 1:1 ratio: 600 pixels
b) 4:5 ratio: 750 pixels
Key Elements to Include in the Ads:

1) Headline: "HOA Violating Your Rights?"
2) Main Message: "We sue HOAs for Homeowners."
3) Firm Name: Lindqvist Harrow, P.A.
4) Website: www.brightgatelegal-example.com
5) Phone Number: 1-800-555-0142
6) Florida Bar Compliance Statement: "Serving Homeowners in Florida with our main office in Miami-Dade."
7) Call-to-Action (CTA): Include a strong CTA such as “Contact us today for a consultation!”
8) Tone and Style: Professional yet approachable. The ad should emphasize trust, expertise, and our dedication to homeowners' rights.
9) Branding: Please use our firm's brand colors and fonts. Ensure that our logo is prominently placed within the ad.
10) Image Suggestions: Consider using images of Florida homes, frustrated homeowners, or visuals that evoke trust, protection, and legal authority.

```html
<!DOCTYPE html>
<html lang="en">
<head>
<meta charset="UTF-8">
<title>Lindqvist Harrow, P.A. — HOA Ad</title>
<link rel="stylesheet" href="https://fonts.googleapis.com/css2?family=Poppins:wght@400;500;600&display=swap">
<style>
  :root {
    --navy: #17177d;
    --navy-deep: #12126a;
    --panel: rgba(196, 192, 232, 0.72);
    --bg-light: #eceaee;
    --bg-mid: #d9d6dc;
    --white: #ffffff;
    --suit-blue: #2a3a66;
    --suit-grey: #6f7177;
  }
  * { margin: 0; padding: 0; box-sizing: border-box; }
  html, body { width: 1200px; height: 1200px; overflow: hidden; }
  body { font-family: "Poppins", sans-serif; color: var(--navy); }

  .ad {
    position: relative;
    width: 1200px;
    height: 1200px;
    overflow: hidden;
    background: var(--bg-light);
  }
  .office-backdrop {
    position: absolute;
    inset: 0;
    background:
      radial-gradient(ellipse at 85% 35%, #9fa0a8 0%, rgba(159,160,168,0) 40%),
      radial-gradient(ellipse at 12% 70%, #e2d9d3 0%, rgba(226,217,211,0) 45%),
      linear-gradient(180deg, #e4e3e6 0%, var(--bg-mid) 45%, #f3f2f4 100%);
  }
  .message-panel {
    position: absolute;
    left: 250px;
    top: 0;
    width: 700px;
    height: 1200px;
    background: var(--panel);
  }
  .brand {
    position: absolute;
    top: 108px;
    left: 250px;
    width: 700px;
    display: flex;
    justify-content: center;
    align-items: center;
    gap: 14px;
  }
  .brand-dot {
    width: 22px; height: 22px; border-radius: 50%;
    background: var(--navy);
  }
  .brand-name {
    font-size: 22px;
    font-weight: 500;
    color: var(--navy);
    letter-spacing: 0.5px;
  }
  .copy {
    position: absolute;
    left: 250px;
    width: 700px;
    text-align: center;
    text-transform: uppercase;
    color: var(--navy);
    font-weight: 500;
  }
  .headline { top: 258px; font-size: 38px; letter-spacing: 0.5px; }
  .main-message { top: 390px; font-size: 36px; line-height: 1.3; }
  .main-message .emphasis { display: block; font-size: 50px; line-height: 1.1; }
  .compliance { top: 578px; font-size: 28px; line-height: 1.5; letter-spacing: 0.3px; }

  .attorneys-photo {
    position: absolute;
    left: 205px;
    top: 683px;
    width: 790px;
    height: 517px;
  }
  .contact-pill {
    position: absolute;
    top: 1092px;
    height: 40px;
    display: flex;
    align-items: center;
    gap: 10px;
    padding: 0 20px 0 4px;
    border-radius: 20px;
    background: var(--navy-deep);
    color: var(--white);
    font-size: 14.5px;
    font-weight: 500;
  }
  .contact-pill .icon {
    width: 32px; height: 32px; border-radius: 50%;
    border: 2px solid var(--white);
    display: flex; align-items: center; justify-content: center;
  }
  .website { left: 69px; }
  .phone { left: 939px; }
</style>
</head>
<body>
  <main class="ad">
    <div class="office-backdrop" role="img" aria-label="Softly blurred law office with attorney and client at a desk"></div>
    <div class="message-panel"></div>

    <div class="brand">
      <span class="brand-dot"></span>
      <span class="brand-name">Lindqvist Harrow, P.A.</span>
    </div>

    <h1 class="copy headline">HOA Violating Your Rights</h1>
    <p class="copy main-message">We sue HOAs for <span class="emphasis">Homeowners</span></p>
    <p class="copy compliance">Serving homeowners in Florida<br>with our main office in Miami-Dade</p>

    <svg class="attorneys-photo" viewBox="0 0 790 517" role="img" aria-label="Portrait of the firm's two attorneys in suits, standing side by side">
      <defs>
        <linearGradient id="suitBlue" x1="0" y1="0" x2="0" y2="1">
          <stop offset="0" stop-color="#35487a"/>
          <stop offset="1" stop-color="#1f2c52"/>
        </linearGradient>
        <linearGradient id="suitGrey" x1="0" y1="0" x2="0" y2="1">
          <stop offset="0" stop-color="#85878d"/>
          <stop offset="1" stop-color="#5b5d63"/>
        </linearGradient>
      </defs>
      <path d="M0 517 L0 330 Q0 230 120 215 L250 215 Q360 230 370 330 L370 517 Z" fill="url(#suitBlue)" opacity="0.9"/>
      <path d="M340 517 L340 320 Q345 220 470 205 L600 205 Q720 220 735 320 L735 517 Z" fill="url(#suitGrey)" opacity="0.9"/>
    </svg>

    <div class="contact-pill website">
      <span class="icon">
        <svg width="18" height="18" viewBox="0 0 24 24" fill="none" stroke="#fff" stroke-width="1.8">
          <circle cx="12" cy="12" r="9"/>
          <ellipse cx="12" cy="12" rx="4" ry="9"/>
          <line x1="3" y1="12" x2="21" y2="12"/>
        </svg>
      </span>
      www.brightgatelegal-example.com
    </div>

    <div class="contact-pill phone">
      <span class="icon">
        <svg width="16" height="16" viewBox="0 0 24 24" fill="#fff">
          <path d="M6.6 10.8a15.1 15.1 0 0 0 6.6 6.6l2.2-2.2a1 1 0 0 1 1-.25 11.4 11.4 0 0 0 3.6.57 1 1 0 0 1 1 1V20a1 1 0 0 1-1 1A17 17 0 0 1 3 4a1 1 0 0 1 1-1h3.5a1 1 0 0 1 1 1c0 1.25.2 2.46.57 3.6a1 1 0 0 1-.25 1z"/>
        </svg>
      </span>
      1-800-555-0142
    </div>
  </main>
</body>
</html>
```